Letterhead for Clean City Delivery Logistics needed

Dear all,

we are looking for a powerful design for our letterhead. We are a Berlin-based (Germany) logistics company which delivers parcel on the last mile in a sustainable way. Design should communicate: sustainability, integrity, one family, performance-focused, passionate for excellence and customer experience. Please find company logo attached.

Looking forward for

```html
<!DOCTYPE html>
<html lang="en">
<head>
<meta charset="utf-8">
<title>Canopy Freight Letterhead</title>
<link href="https://fonts.googleapis.com/css2?family=Montserrat:wght@400;500;600&display=swap" rel="stylesheet">
<style>
  :root {
    --backdrop: #8a8a8a;
    --paper: #f6f5f6;
    --forest: #0f8c35;
    --lime: #a3c316;
    --ink: #1d1d1d;
    --watermark: #ebefe8;
  }
  html, body {
    margin: 0;
    width: 1200px;
    height: 1155px;
    overflow: hidden;
    background: var(--backdrop);
  }
  .letterhead {
    position: absolute;
    left: 206px;
    top: 20px;
    width: 788px;
    height: 1115px;
    background: var(--paper);
    box-shadow: 0 6px 24px rgba(0,0,0,0.35);
    overflow: hidden;
  }
  .brand {
    position: absolute;
    left: 62px;
    top: 96px;
    display: flex;
    align-items: center;
    gap: 14px;
  }
  .brand-dot {
    width: 48px;
    height: 48px;
    border-radius: 50%;
    background: var(--forest);
    flex: none;
  }
  .brand-name {
    font-family: "Montserrat", sans-serif;
    font-weight: 600;
    font-size: 28px;
    line-height: 1.1;
    color: var(--forest);
  }
  .brand-tagline {
    font-family: "Montserrat", sans-serif;
    font-weight: 500;
    font-size: 12px;
    color: var(--forest);
    letter-spacing: 0.6px;
    margin-top: 4px;
  }
  .contact {
    position: absolute;
    right: 62px;
    top: 62px;
    padding-left: 14px;
    border-left: 1.5px solid var(--forest);
    font-family: "Montserrat", sans-serif;
    font-style: normal;
    font-size: 12.5px;
    line-height: 1.35;
    color: var(--ink);
  }
  .contact-address { font-weight: 500; margin: 0 0 4px; }
  .contact-line { display: flex; align-items: center; gap: 7px; margin: 0; }
  .contact-line svg { width: 11px; height: 11px; fill: var(--forest); flex: none; }
  .watermark {
    position: absolute;
    left: 214px;
    top: 380px;
    width: 360px;
    height: 360px;
    border-radius: 50%;
    background: var(--watermark);
  }
  .footer-rule {
    position: absolute;
    left: 0;
    right: 0;
    bottom: 70px;
    height: 6px;
    background: var(--lime);
  }
  .footer-band {
    position: absolute;
    left: 0;
    right: 0;
    bottom: 0;
    height: 58px;
    background: var(--forest);
  }
</style>
</head>
<body>
  <main class="letterhead">
    <header class="brand">
      <span class="brand-dot"></span>
      <div>
        <div class="brand-name">Canopy Freight</div>
        <div class="brand-tagline">Clean City Delivery</div>
      </div>
    </header>

    <address class="contact">
      <p class="contact-address">48 Linden Row, Unit 7,<br>Berlin 10115</p>
      <p class="contact-line">
        <svg viewBox="0 0 24 24"><path d="M6.6 10.8a15 15 0 0 0 6.6 6.6l2.2-2.2a1 1 0 0 1 1-.25 11.4 11.4 0 0 0 3.6.57 1 1 0 0 1 1 1V20a1 1 0 0 1-1 1A17 17 0 0 1 3 4a1 1 0 0 1 1-1h3.5a1 1 0 0 1 1 1c0 1.25.2 2.45.57 3.57a1 1 0 0 1-.25 1z"/></svg>
        (030) 555-0142
      </p>
      <p class="contact-line">
        <svg viewBox="0 0 24 24"><path d="M2 5h20v14H2z M2 5l10 8 10-8" fill="none" stroke="#0f8c35" stroke-width="2.4"/></svg>
        hello@canopyfreight.test
      </p>
      <p class="contact-line">
        <svg viewBox="0 0 24 24"><circle cx="12" cy="12" r="10"/></svg>
        www.canopyfreight.test
      </p>
    </address>

    <div class="watermark"></div>

    <div class="footer-rule"></div>
    <div class="footer-band"></div>
  </main>
</body>
</html>
```